Beauty Salon Industry - Web Design Project

zTrellis is a well-funded start up developing an Online Marketing Platform for small businesses in Europe.
We require a large number of high quality business web designs for our business website builder. Our business websites are seamlessly integrated into our Online Marketing systems and therefore it is important for designers to comply with our Design Guidelines.
This is our second contest and it will focus on the beauty salon industry. We will be running contents every 2-3 weeks for a new industry. Last month, we ran a contest for Builder website designs with 3 top prizes (plus £10 per variation) and we also paid out £25 per design for 20+ entries from designers who did not win the top prizes. So we encourage all entries!
We have included a wire frame this time to encourage you to be as creative as possible with your designs and layout while respecting the following guidelines:
1) You CAN change the layout as much as you like. If you think a vertical menu would look better, then use it. If you think the design would benefit from moving an element to a different location, then you can do that too.
2) You must include ALL the elements in the wire frame in your design.(e.g. latest 2 news entries, a testimonial, 1 gallery image, carousel etc...). Please make sure you have looked through the wire frame and know what is required. Entries that do not include all the elements will not qualify to win.
3) So remember, you CAN change the layout as much as you like but DO NOT remove any elements nor move them to a different page.
4) You may change the size and style of the carousel image. We would like to see as many variations of this as possible.
We are rewarding 3 prizes, and would like the winning designer to design the internal pages to the new design.
As always, if we think your designs could be incorporated into our system, but you do not win the competition, we will reward £25. Therefore, we encourage designers to submit as many designs as possible as we may award up to 25 designs.
Judging criteria : -
1) Visual Design
2) Layout must adhere to best practices and wireframe. If you decide to move elements around significantly please provide reason
3) Functional, informative and drives calls to action
Updates
As usual:
1st place = £350
2nd place = £250
3rd place = £150
Good luck!
Very happy with all the designs submitted so far, and will provide feedback ASAP.
We would like to see you try arranging the elements differently. So please try different navigation types and layouts.
Thanks
Morris
Prize funds for 1st place has been slightly increased.
Thanks
Morris
We have already had some amazing designs submitted. Thanks.
Remember to play with the layout of the elements and try designs with a carousel/slider that is in portrait not just in landscape.
Thanks everyone!
Morris
Hi everyone, we are really enjoying looking through the designs.
We have one NEW requirement. If you have used an image from http://www.quarnex-demo.net/ in your design, could you please replace it with another.
We are not associated with them.
Thank you.
I have just sent a poll around the office to vote on all the designs and hope to have the results soon.
Good luck and I hope to see all your great designs for our next project in a couple of weeks.
Morris
Hi everyone, we hope you have had a good holiday season. We will be rewarding the prizes very soon, hopefully today or tomorrow.
Thanks
Morris
We are currently going through all the designs that did not win our competition and will be contacting the designers of the designs we would like to use in our system, so please keep an eye on your inbox over the next few days.
Thank you
Morris
Target Market(s)
Beauty Salon Industry
Industry/Entity Type
Beauty Salon
Look and feel
Each slider illustrates characteristics of the customer's brand and the style your logo design should communicate.

```html
<!DOCTYPE html>
<html lang="en">
<head>
<meta charset="utf-8">
<title>Lumora – Hair and Urban Spa</title>
<link rel="stylesheet" href="https://fonts.googleapis.com/css2?family=Arimo:wght@400;700&family=Roboto+Condensed:wght@700&family=Lora:ital@1&display=swap">
<style>
:root{
  --bg:#eceef1;
  --brown-dark:#2a120d;
  --brown:#5a1a10;
  --brown-mid:#7a2414;
  --cream:#f7f3ee;
  --text:#333;
  --muted:#555;
  --link:#1a5fd6;
  --hour:#8a1020;
  --white:#fff;
}
*{margin:0;padding:0;box-sizing:border-box}
html,body{width:987px;height:1200px;overflow:hidden}
body{position:relative;background:var(--bg);font-family:Arimo,Arial,sans-serif;color:var(--text)}
.abs{position:absolute}
.header{left:0;top:0;width:987px;height:156px;background:radial-gradient(ellipse at 50% 40%,#4a2219 0%,var(--brown-dark) 75%)}
.brand{left:172px;top:36px;color:var(--white)}
.brand-mark{display:inline-block;width:34px;height:34px;border-radius:50%;background:var(--white);vertical-align:middle;margin-right:10px}
.brand-name{font-family:Arimo,Arial,sans-serif;font-weight:700;font-size:36px;vertical-align:middle}
.brand-tag{display:block;font-family:Lora,Georgia,serif;font-style:italic;font-size:20px;color:#ddd;margin:2px 0 0 52px}
.book{left:690px;top:84px;width:150px;height:44px;border-radius:22px 22px 22px 22px;background:linear-gradient(#8a2a1a,#4f150c);color:var(--white);text-align:center;box-shadow:0 2px 4px rgba(0,0,0,.5)}
.book small{display:block;font-size:13px;margin-top:5px}
.book strong{display:block;font-family:"Roboto Condensed",sans-serif;font-size:17px;letter-spacing:.5px}
.phone-icon{left:668px;top:68px}
.nav{left:126px;top:134px;width:736px;height:44px;border-radius:22px;background:linear-gradient(#fff,#e6e7ea);box-shadow:0 1px 3px rgba(0,0,0,.25)}
.nav a{position:absolute;top:11px;height:24px;line-height:24px;font-family:"Roboto Condensed",sans-serif;font-size:12.5px;color:#222;text-decoration:none;text-align:center}
.nav .active{background:var(--brown);color:var(--white);border-radius:12px}
.nav .hover{border:2px solid #c5ccd6;border-radius:12px;background:#eef0f3}
.slider{left:131px;top:210px;width:539px;height:360px;border-radius:6px;background:radial-gradient(ellipse at 60% 45%,#7a3a9a 0%,#555 35%,#2c2c2c 100%)}
.arrow{width:27px;height:27px;border-radius:50%;background:#fff;box-shadow:0 1px 3px rgba(0,0,0,.5)}
.arrow.next{background:#4a8ad0}
.testimonial{left:131px;top:580px;width:539px;height:92px;border-radius:6px;background:var(--brown-dark);color:#eee}
.testimonial q{position:absolute;left:11px;top:8px;width:520px;font-family:Lora,Georgia,serif;font-style:italic;font-size:14px;line-height:17px;quotes:"“" "”"}
.testimonial cite{position:absolute;left:0;width:100%;top:50px;text-align:center;font-family:Lora,Georgia,serif;font-size:10.5px;color:#ccc}
.pill{display:block;height:24px;line-height:24px;border-radius:12px;font-size:11px;text-align:center;color:#333;background:linear-gradient(#fff,#e2e4e8);box-shadow:0 1px 2px rgba(0,0,0,.3);text-decoration:none}
.pill.dark{background:var(--brown);color:#fff}
.intro{left:132px;top:702px;width:232px}
.intro h2{font-size:14px;font-weight:400;line-height:16px;color:#222}
.intro p{font-size:9px;line-height:14px;color:var(--muted);margin-top:14px;text-align:justify}
.news{left:377px;width:294px}
.news h3{font-size:14px;font-weight:400;color:#222}
.news p{font-size:9px;line-height:14px;color:var(--muted);margin-top:6px}
.news a{color:var(--link);text-decoration:none}
.news .meta{font-size:9px;color:#444;margin-top:14px}
.news .meta span{margin-left:70px}
.bubble{display:inline-block;width:12px;height:11px;border-radius:50%;background:#9cc4ec;vertical-align:middle;margin-right:5px}
.rule{height:0;border-top:1px solid #aaa}
.dotted{border-top:1px dotted #999}
.partner{top:984px;height:64px;line-height:64px;text-align:center;font-size:17px;color:#666}
.partner.box{background:#666;color:#fff}
.panel{left:686px;width:170px;background:#f4f5f7;border:1px solid #d8dadd;border-radius:3px}
.panel h4{height:30px;line-height:30px;background:linear-gradient(#7a2414,#4a140c);color:#fff;text-align:center;font-weight:400;font-size:14px}
.panel .txt{font-size:10px;color:#222;line-height:12px}
.hours{font-size:10.5px;color:#222}
.hours div{position:absolute;left:16px;width:150px}
.hours b{position:absolute;left:72px;font-weight:400;color:var(--hour)}
.footer{left:0;top:1110px;width:987px;height:90px;background:var(--brown-dark)}
.footer nav a{position:absolute;top:24px;font-size:8.5px;color:#aaa;text-decoration:none}
.footer p{position:absolute;left:134px;top:44px;font-size:9px;color:#999;letter-spacing:.3px}
.foot-brand{left:688px;top:20px;color:#6e5a55}
</style>
</head>
<body>
<header class="abs header">
  <div class="abs brand"><span class="brand-mark"></span><span class="brand-name">Lumora</span><span class="brand-tag">Hair and Urban Spa</span></div>
  <svg class="abs phone-icon" width="40" height="66" viewBox="0 0 40 66"><path d="M30 6c-6 0-14 10-18 24s-4 24 0 28l6-2c-3-4-2-14 1-24s8-18 12-20z" fill="#222" stroke="#666" stroke-width="1.5"/></svg>
  <a class="abs book"><small>BOOK NOW</small><strong>020 7946 0312</strong></a>
</header>

<nav class="abs nav">
  <a class="active" style="left:70px;width:74px">HOME</a>
  <a style="left:156px;width:70px">SERVICES</a>
  <a class="hover" style="left:242px;width:68px">GALLERY</a>
  <a style="left:328px;width:110px">TESTIMONIALS</a>
  <a style="left:446px;width:60px">NEWS</a>
  <a style="left:516px;width:80px">ABOUT US</a>
  <a style="left:608px;width:90px">CONTACT US</a>
</nav>

<div class="abs slider" role="img" aria-label="Carousel photo of a woman with vivid purple hair lying on a dark textured rug"></div>
<div class="abs arrow" style="left:156px;top:532px"><svg width="27" height="27"><path d="M16 8l-6 5.5 6 5.5" stroke="#333" stroke-width="3" fill="none"/></svg></div>
<div class="abs arrow next" style="left:196px;top:532px"><svg width="27" height="27"><path d="M11 8l6 5.5-6 5.5" stroke="#123" stroke-width="3" fill="none"/></svg></div>

<blockquote class="abs testimonial">
  <q>My hairstylist, Annika, was truly amazing. She listened to exactly what i wanted, but also told me exactly what....</q>
  <cite>- Mira Kessel -</cite>
  <a class="pill abs" style="left:466px;top:57px;width:67px">More →</a>
</blockquote>

<section class="abs intro">
  <h2>LET OUR HAIR AND BEAUTY SKILLS BLOW&nbsp; YOU AWAY</h2>
  <p>Lumora is a passionate, creative team, dedicated to delivering a second to none, personal salon experience that will 'blow' your mind.</p>
  <p>Where ultimate hairdressing comes hand-in-hard with style, glamour, fashion, innovation and skill to create an exquisite salon experience in the heart of London.</p>
</section>
<a class="abs pill dark" style="left:294px;top:866px;width:66px">More →</a>

<article class="abs news" style="top:700px">
  <h3>Book Now for Christmas</h3>
  <p>Our salon is usually very busy for the two weeks before Christmas, so please book early: call <a>020 7946 0312</a>, or contact us.</p>
  <div class="meta">1 Dec, 2011 <span><i class="bubble"></i>By. <a>Admin</a></span></div>
</article>
<div class="abs dotted" style="left:377px;top:790px;width:294px"></div>
<article class="abs news" style="top:801px">
  <h3>Want to be a hair model?</h3>
  <p>We always need models for our portfolio. If you want to become one, please contact us, or call <a>020 7946 0312</a></p>
  <div class="meta">9 Dec, 2011 <span><i class="bubble"></i>By. <a>Admin</a></span></div>
</article>
<a class="abs pill" style="left:592px;top:883px;width:78px">More news →</a>

<div class="abs rule" style="left:131px;top:944px;width:540px"></div>
<div class="abs partner" style="left:131px;width:110px">Maison Clair</div>
<div class="abs partner" style="left:280px;width:110px;font-weight:700">Velora</div>
<div class="abs partner" style="left:410px;width:100px">Fern &amp; Fable</div>
<div class="abs partner box" style="left:554px;width:112px;font-size:14px">Hartwell Pro</div>

<aside>
  <section class="abs panel" style="top:211px;height:241px">
    <h4>News Entry</h4>
    <div class="abs" style="left:25px;top:44px;width:118px;height:141px;border:1px solid #aaa;background:linear-gradient(#f0f0f0,#c33 60%,#e0e0e0)" role="img" aria-label="Red hair care product bottles"></div>
    <div class="abs" style="left:5px;top:34px;width:50px;height:50px;border-radius:50%;background:#e85a1c;color:#fff;font-weight:700;font-size:16px;line-height:50px;text-align:center">£25</div>
    <div class="abs txt" style="left:27px;top:192px">Complimentary gift<br>for first-time clients!</div>
    <div class="abs txt" style="left:27px;top:220px;color:var(--brown);font-weight:700">Book Appointment Now</div>
  </section>
  <section class="abs panel" style="top:464px;height:224px">
    <h4>Blow Address</h4>
    <div class="abs" style="left:11px;top:41px;width:146px;height:104px;background:linear-gradient(135deg,#f3ecd6,#e9e0c4);border:1px solid #ccc" role="img" aria-label="Street map of the salon location"></div>
    <div class="abs txt" style="left:0;top:161px;width:100%;text-align:center;font-size:10.5px">12 Harrow Lane - London<br>W1X 2QZ</div>
    <a class="abs pill" style="left:28px;top:191px;width:106px">View large map →</a>
  </section>
  <section class="abs panel hours" style="top:700px;height:174px">
    <h4>Bussiness Hour</h4>
    <div style="top:44px">Monday<b>9 a.m - 5 p.m</b></div>
    <div style="top:63px">Tuesday<b>9 a.m - 5 p.m</b></div>
    <div style="top:83px">Wednesday<b>9 a.m - 5 p.m</b></div>
    <div style="top:102px">Thursday<b>9 a.m - 5 p.m</b></div>
    <div style="top:122px">Friday<b>9 a.m - 5 p.m</b></div>
    <div style="top:141px">Saturday<b>9 a.m - 5 p.m</b></div>
  </section>
  <div class="abs" style="left:694px;top:888px;width:154px;height:160px;border:2px solid #bbb;background:radial-gradient(ellipse at 50% 45%,#8a6a55,#5e4a3e 70%)" role="img" aria-label="Gallery photo of a model with a sculptural floral headpiece"></div>
  <a class="abs pill" style="left:728px;top:1069px;width:90px">View Gallery →</a>
</aside>

<footer class="abs footer">
  <nav>
    <a style="left:133px;color:#fff">HOME</a><a style="left:174px">SERVICES</a><a style="left:229px">GALLERY</a><a style="left:281px">TESTIMONIALS</a><a style="left:358px">NEWS</a><a style="left:402px">ABOUT US</a><a style="left:460px">CONTACT US</a><a style="left:530px">SITE MAP</a>
  </nav>
  <p>Copyright © 2011 LUMORA limited. All rights reserved.&nbsp; Managed by zTrellis.com&nbsp;&nbsp; I &nbsp; <span style="color:#7a5a55">Admin</span></p>
  <div class="abs foot-brand"><span style="display:inline-block;width:24px;height:24px;border-radius:50%;background:#6e5a55;vertical-align:middle;margin-right:6px"></span><span style="font-weight:700;font-size:24px;vertical-align:middle">Lumora</span><span style="display:block;font-family:Lora,Georgia,serif;font-style:italic;font-size:14px;margin:2px 0 0 36px">Hair and Urban Spa</span></div>
</footer>
</body>
</html>
```